Meridale Cleaning Services

In need of a business card design suited for a growing cleaning company.

We offer our cleaning and maintenance services to a wide range of clients including but not limited to the following: constuction industry, hospitality, commercial, industrial and domestic

I want the card to be very noticable, i would like people to say 'hey, great card!' when i hand them my card.double sided would be nice

we want our business to come across as exceedingly professional and innovative (different).

a contemporary design is what we have in mind
we want to present an image of a quality business with a high standard of excellence in consistent service.

i just really need a card that persuades top end quality,
our business is very certified and also strives towards environmentaly friendly alternatives
Updates

hey sorry, i have uploaded my company logo design and name
cheers.

hey guys i have added my company logo/name file on my brief page. many thanks

sorry guys a typo in the brief..
address is Tolley Rd. not Tolly Rd
thanks

Industry/Entity Type

Industrial

Requirements
Must have
• company name: meridale cleaning services
operations manager: Colm Varetti
Tel: (02)9373 6204
Fax: (02)8645 7712
Mob: 0438571490

address: 47 Tolly RD Lindcove NSW 2081
Postal Adress: PO Box 5832 Harwell Park NSW 2119
email: meridaleclean@wexanet.com.au
website: meridalecleaningservices.com.au

```html
<!DOCTYPE html>
<html lang="en">
<head>
<meta charset="utf-8">
<title>Meridale Cleaning Services — Business Card</title>
<link href="https://fonts.googleapis.com/css2?family=Arimo:wght@400;700&display=swap" rel="stylesheet">
<style>
  :root {
    --stage: #5a5a5c;
    --brand-blue: #1b7fc4;
    --brand-green: #8cc63f;
    --paper: #ffffff;
    --ink-light: #ffffff;
    --ink-soft: #e4f0fa;
  }
  * { margin: 0; padding: 0; box-sizing: border-box; }
  html, body {
    width: 1200px; height: 900px; overflow: hidden;
    background: var(--stage);
    font-family: "Arimo", Arial, sans-serif;
  }
  .stage {
    position: relative; width: 1200px; height: 900px;
  }
  .card {
    position: absolute; top: 295px;
    width: 540px; height: 310px;
    overflow: hidden;
    box-shadow: 0 6px 18px rgba(0,0,0,0.35);
  }
  .card-back { left: 50px; }
  .card-front { left: 610px; }
  .card-art { position: absolute; inset: 0; display: block; }

  /* back side */
  .logo-plate {
    position: absolute; left: 342px; top: 50px;
    width: 170px; height: 56px;
    background: var(--paper);
    display: flex; align-items: center; gap: 8px;
    padding: 0 10px;
  }
  .logo-dot {
    width: 30px; height: 30px; border-radius: 50%;
    background: var(--brand-blue); flex: none;
  }
  .logo-plate .brand-name {
    color: var(--brand-blue); font-weight: 700; line-height: 1;
  }
  .logo-plate .brand-main { display: block; font-size: 21px; }
  .logo-plate .brand-sub { display: block; font-size: 8.5px; letter-spacing: 0.3px; margin-top: 2px; }

  .address-block {
    position: absolute; left: 33px; top: 170px;
    color: var(--ink-light); font-size: 11.5px; line-height: 20.5px;
    list-style: none;
  }

  /* front side */
  .brand-lockup {
    position: absolute; left: 46px; top: 172px;
    display: flex; align-items: center; gap: 12px;
  }
  .brand-mark {
    width: 66px; height: 66px; border-radius: 50%;
    background: var(--brand-blue); flex: none;
  }
  .brand-lockup .brand-name {
    color: var(--brand-blue); font-weight: 700; line-height: 1;
  }
  .brand-lockup .brand-main { display: block; font-size: 38px; }
  .brand-lockup .brand-sub { display: block; font-size: 12.5px; letter-spacing: 0.6px; margin-top: 3px; }

  .contact-person {
    position: absolute; right: 26px; top: 118px;
    text-align: right; color: var(--ink-light);
  }
  .person-name { font-size: 18px; font-weight: 400; }
  .person-role { font-size: 12.5px; margin-top: 2px; }
  .contact-lines {
    position: absolute; right: 26px; top: 176px;
    list-style: none; text-align: right;
    color: var(--ink-soft); font-size: 11.5px; line-height: 20px;
  }
</style>
</head>
<body>
<main class="stage">

  <section class="card card-back" aria-label="Business card, back">
    <svg class="card-art" viewBox="0 0 540 310" preserveAspectRatio="none" aria-hidden="true">
      <rect width="540" height="310" fill="var(--brand-blue)"/>
      <path d="M290 0 C250 60 370 110 350 175 C335 235 300 270 320 310 L540 310 L540 0 Z" fill="var(--brand-green)"/>
    </svg>
    <div class="logo-plate">
      <span class="logo-dot"></span>
      <span class="brand-name">
        <span class="brand-main">Meridale</span>
        <span class="brand-sub">CLEANING SERVICES</span>
      </span>
    </div>
    <ul class="address-block">
      <li>Address: 47 Tolley RD Lindcove NSW 2081</li>
      <li>Postal Adress: PO Box 5832 Harwell Park NSW 2119</li>
      <li>Email: meridaleclean@wexanet.com.au</li>
      <li>Website: meridalecleaningservices.com.au</li>
    </ul>
  </section>

  <section class="card card-front" aria-label="Business card, front">
    <svg class="card-art" viewBox="0 0 540 310" preserveAspectRatio="none" aria-hidden="true">
      <rect width="540" height="310" fill="var(--paper)"/>
      <path d="M280 0 C250 60 375 105 355 175 C340 235 305 270 318 310 L540 310 L540 0 Z" fill="var(--brand-blue)"/>
    </svg>
    <div class="brand-lockup">
      <span class="brand-mark"></span>
      <span class="brand-name">
        <span class="brand-main">Meridale</span>
        <span class="brand-sub">CLEANING SERVICES</span>
      </span>
    </div>
    <div class="contact-person">
      <p class="person-name">Colm Varetti</p>
      <p class="person-role">operations manager</p>
    </div>
    <ul class="contact-lines">
      <li>Tel: (02)9373 6204</li>
      <li>Fax: (02)8645 7712</li>
      <li>Mob: 0438571490</li>
    </ul>
  </section>

</main>
</body>
</html>
```